KiteSurf Weather App Forecast Screen re-design (1 Screen)

We are redesigning our application, BreezeLoom. Our main screen is the forecast screen. The forecast screen presents the forecast for multiple places for the selected day.

Intro
-----

The user has a list of favorite spots that he is monitoring. Then he selects the date that he wants to get the forecast. The forecast screen presents a list of all the spots and a summary of the weather conditions. Spots are sorted by weather conditions. At the top, he gets the spot with the best weather conditions. We have an algorithm that can evaluate whether given weather conditions are good or not. When they are good we indicate that to the user.

Current Solution
------------------

There is also a landscape version, which contains a bit more data: "Current Forecast Screen Lanscape.jpeg". The landscape one is a bit funny, as it is taken from an Zentra Q and the app was not designed for it at the time.

The bars that you see for each hour use our algorithm to display whether the conditions are good:

- When the color is gray the conditions are not good
- When the color is yellow there are light wind conditions
- When the color is green there are good
- When the color is red the wind is very strong
- The height of the bar indicates wind strength

More Info
-----------

The detailed forecast screen is also attached so you can get a bit more context, "DetailedForecast.jpeg"

An example from an application that has a similar chart is attached, "SimilarApp.jpeg". I have circled the chart with red.

Future Solution
------------------

(See note.jpeg)

We want to create a page that contains more information and passes a better message to our users.

The elements that are important and we want to present to the user are the following:

1. Wind. (The most important)
It contains two elements: strength and direction.

1.1 Wind Strength.
Good wind strength is anything between 10-45 knots (measurement unit like km/h). The best representation with a color palette.
Gray will be the color used when the strength is not between 10-45.
The palette should start with yellow at 10 knots, then move toward green for 22knots and finally go towards red for 45 knots.

1.2 Wind Direction.
There are good wind directions that we can kite and directions that is is not possible.
Can be presented by an arrow that points in the direction the wind is blowing to. The color of the arrow will be green when the direction is good, yellow when it is average and gray when it is not good.

My thought for portrait mode is to use an arrow point for the direction and the color of the arrow to represent the strength. Solution number 2 on my notes. Then for landscape, we could use both a number and an arrow like number 4 on my notes.

2. Wave.
It contains three elements: height, period and direction. It is not displayed to all of our users only the ones that have selected the wave riding option.

2.1 Height is represented by a number. Ex. 1.2 meters or 2 foot.
2.2 Period is represented in seconds. Ex. 12 seconds.
2.3 Directions is an arrow that points to the direction the wave is coming from.

Again the solution should be like the wind. Arrow for direction and the color of the arrow for height. The palette here should be something with different blue colors.

3. Tide height. (Optional for tidal spots, as not all spots have tides)

The best way to represent that it through a graph. I would also like to see an alternative, where we have three symbols for low, mid and high tide.

4. General Weather. Rain/Snow and temperature.

This should be represented by a sun/cloud/rain symbol. If it is very cold the symbol can also contain an ice sign on the background.

---------

This is a guideline creativity will be valued. Maybe there is another way to do it that I have not thought about.

The winner of the competition will have to send us all graphics used in vector format, so we can input them to our xCode project.

Finally the person that wins the competition will be the first one to be considered for the redesign of the rest of our application.

Target Market(s)

Kitesurfers

Font styles to use
Sans Serif

Colors

Designer to choose colors to be used in the design.

Requirements
Must have
• It should be minimal and clearly communicate the weather forecast to my users. It should be user friendly.
Nice to have
• Communicative color palettes for both wind strength, tide and waves
Should not have
• Hard to understand UI

```html
<!DOCTYPE html>
<html lang="en">
<head>
<meta charset="utf-8">
<title>GustLine Weather App – BreezeLoom forecast screens</title>
<link href="https://fonts.googleapis.com/css2?family=Roboto:wght@300;400;500;700;900&display=swap" rel="stylesheet">
<style>
:root{
  --stage:#6f8fb6;
  --brand-teal:#6fcfc0;
  --white:#ffffff;
  --ink:#2b3a44;
  --ink-soft:#5d6d78;
  --teal-top:#7fd6c8;
  --teal-mid:#a9e4dc;
  --teal-deep:#4e8f8d;
  --panel:#2f5e5f;
  --sky-top:#9fd9f2;
  --sky-low:#dcecf3;
  --accent-blue:#52c2f0;
  --good:#5fd3a8;
  --light:#f2d21c;
  --strong:#e8244f;
  --calm:#d9dde0;
  --card-a:#7e98a6;
  --card-b:#c9dbe3;
}
*{box-sizing:border-box;margin:0;padding:0}
html,body{width:1200px;height:1040px;overflow:hidden}
body{background:var(--stage);font-family:"Roboto",sans-serif;position:relative;color:var(--ink)}

.hero-title{position:absolute;left:56px;top:28px;line-height:1}
.hero-title .brand{display:block;font-weight:900;font-size:128px;color:var(--brand-teal);letter-spacing:-3px}
.hero-title .sub{display:block;font-weight:400;font-size:68px;color:var(--white);margin-top:4px}

.screen{position:absolute;width:360px;border-radius:40px;overflow:hidden;box-shadow:0 24px 50px rgba(20,40,70,.35)}
.status{position:absolute;top:14px;left:26px;right:26px;display:flex;justify-content:space-between;font-size:13px;font-weight:500;color:var(--ink)}
.icon{display:block}

/* ---------- spot detail screen ---------- */
.spot-screen{left:110px;top:290px;height:720px;background:linear-gradient(180deg,var(--teal-top) 0%,var(--teal-mid) 38%,var(--teal-deep) 100%)}
.spot-header{position:absolute;top:44px;left:20px;right:20px;height:28px}
.spot-header .back{position:absolute;left:0;top:4px}
.spot-header .title{position:absolute;left:0;right:0;text-align:center;top:6px;font-size:14px;font-weight:500;letter-spacing:1px;color:var(--ink)}
.spot-header .add{position:absolute;right:36px;top:2px}
.spot-header .pin{position:absolute;right:0;top:2px}
.avatar{position:absolute;right:22px;top:86px;width:38px;height:38px;border-radius:50%;background:radial-gradient(circle at 40% 40%,#c98b6b,#6b4a3a)}
.follow{position:absolute;right:72px;top:94px;background:#a9e0f5;color:var(--white);font-size:12px;font-weight:500;padding:5px 16px;border-radius:14px}
.stats{position:absolute;left:28px;top:138px;display:flex;gap:34px}
.stat b{display:block;font-size:15px;font-weight:500;color:var(--white)}
.stat span{font-size:9px;color:var(--white);opacity:.85}
.fav-heart{position:absolute;right:26px;top:146px}
.spot-name{position:absolute;left:26px;top:186px;font-size:42px;font-weight:300;color:var(--white)}
.temp{position:absolute;left:24px;top:242px;font-size:66px;font-weight:300;color:var(--white)}
.now{position:absolute;left:168px;top:252px;right:20px;display:flex;justify-content:space-between;color:var(--white)}
.now .item b{display:block;font-size:18px;font-weight:500}
.now .item span{font-size:11px;opacity:.9}
.now .wx{display:flex;gap:6px;margin-top:4px}
.forecast-caption{position:absolute;left:26px;top:330px;font-size:12px;color:var(--white)}
.forecast-panel{position:absolute;left:14px;right:14px;top:356px;height:270px;border-radius:18px;overflow:hidden;background:linear-gradient(180deg,#3f6f6f 0%,var(--panel) 55%,#294a45 100%)}
.forecast-panel svg{position:absolute;inset:0}

.tabbar{position:absolute;left:0;right:0;bottom:0;height:78px}
.tab{position:absolute;bottom:18px;font-size:10px;text-align:center;color:var(--ink)}
.tab .icon{margin:0 auto 3px}
.tab.explore{left:30px}
.tab.favorites{right:26px}
.tab.calendar{left:148px;bottom:0;width:64px;height:74px;background:var(--accent-blue);border-radius:16px 16px 0 0;display:flex;align-items:center;justify-content:center}

/* ---------- daily outlook screen ---------- */
.outlook-screen{left:650px;top:150px;height:860px;background:linear-gradient(180deg,var(--sky-top) 0%,var(--sky-low) 100%)}
.outlook-header{position:absolute;top:46px;left:20px;right:20px;height:28px}
.outlook-header .menu{position:absolute;left:0;top:4px}
.outlook-header .title{position:absolute;left:0;right:0;text-align:center;top:6px;font-size:14px;font-weight:500;letter-spacing:1px}
.outlook-header .add{position:absolute;right:36px;top:2px}
.outlook-header .pin{position:absolute;right:0;top:2px}
.spot-list{position:absolute;left:12px;right:12px;top:90px}
.spot-card{position:relative;height:128px;margin-bottom:10px;border-radius:18px;overflow:hidden}
.spot-card .photo{position:absolute;inset:0;background:linear-gradient(160deg,var(--card-b) 0%,var(--card-a) 100%)}
.spot-card.is-green .photo{background:linear-gradient(180deg,#c9dbe3 0%,#8fb0a0 55%,#4f7a45 100%)}
.spot-card .info{position:absolute;left:16px;top:16px;color:var(--white)}
.spot-card h3{font-size:16px;font-weight:500}
.badges{display:flex;gap:5px;margin-top:6px}
.badge{font-size:9px;font-weight:500;padding:2px 6px;border-radius:4px;color:var(--white)}
.badge.live{background:var(--good)}
.badge.good{background:var(--good)}
.badge.light{background:var(--light);color:var(--ink)}
.badge.strong{background:var(--strong)}
.badge.bad{background:#8a9197}
.spot-card .dist{font-size:14px;margin-top:10px}
.spot-card .heart{margin-top:8px}
.spot-card .chart{position:absolute;right:12px;bottom:10px}
.hours-label{font-size:8px;fill:var(--white)}
</style>
</head>
<body>

<h1 class="hero-title"><span class="brand">GustLine</span><span class="sub">Weather App</span></h1>

<!-- Spot detail screen -->
<section class="screen spot-screen" aria-label="Spot detail forecast">
  <div class="status"><span>9:41</span>
    <svg class="icon" width="46" height="12" viewBox="0 0 46 12"><g fill="#2b3a44"><rect x="0" y="8" width="3" height="4"/><rect x="5" y="5" width="3" height="7"/><rect x="10" y="2" width="3" height="10"/><path d="M18 5a9 9 0 0 1 12 0l-2 2a6 6 0 0 0-8 0z"/><rect x="33" y="2" width="12" height="8" rx="2"/></g></svg>
  </div>
  <div class="spot-header">
    <svg class="icon back" width="22" height="16" viewBox="0 0 22 16"><path d="M21 8H2M8 2 2 8l6 6" fill="none" stroke="#2b3a44" stroke-width="2"/></svg>
    <div class="title">MARROWBY</div>
    <svg class="icon add" width="20" height="20" viewBox="0 0 20 20"><circle cx="10" cy="10" r="8.5" fill="none" stroke="#2b3a44" stroke-width="1.5"/><path d="M10 5v10M5 10h10" stroke="#2b3a44" stroke-width="1.5"/></svg>
    <svg class="icon pin" width="16" height="20" viewBox="0 0 16 20"><path d="M8 0a7 7 0 0 1 7 7c0 5-7 13-7 13S1 12 1 7a7 7 0 0 1 7-7z" fill="#1d2830"/><circle cx="8" cy="7" r="2.5" fill="#fff"/></svg>
  </div>
  <div class="avatar" role="img" aria-label="Profile picture of the spot owner"></div>
  <div class="follow">Follow</div>
  <div class="stats">
    <div class="stat"><b>05</b><span>Home</span></div>
    <div class="stat"><b>154</b><span>Following</span></div>
    <div class="stat"><b>54</b><span>Kts away</span></div>
  </div>
  <svg class="icon fav-heart" width="18" height="16" viewBox="0 0 18 16"><path d="M9 15S1 10 1 5a4 4 0 0 1 8-1 4 4 0 0 1 8 1c0 5-8 10-8 10z" fill="#fff"/></svg>
  <div class="spot-name">Saltcombe</div>
  <div class="temp">8°C</div>
  <div class="now">
    <div class="item"><b>1.6m</b><span>Tide</span></div>
    <div class="item"><b>0</b><span>Kts</span></div>
    <div class="item"><b>-</b><span>m²</span>
      <div class="wx">
        <svg class="icon" width="18" height="14" viewBox="0 0 18 14"><path d="M4 12h10a3 3 0 0 0 0-6 5 5 0 0 0-9-1 3.5 3.5 0 0 0-1 7z" fill="none" stroke="#fff" stroke-width="1.3"/></svg>
        <svg class="icon" width="18" height="14" viewBox="0 0 18 14"><circle cx="6" cy="5" r="3" fill="none" stroke="#fff" stroke-width="1.3"/><path d="M6 13h9a2.5 2.5 0 0 0 0-5 4 4 0 0 0-8 0" fill="none" stroke="#fff" stroke-width="1.3"/></svg>
      </div>
    </div>
  </div>
  <div class="forecast-caption">Thursday 21 hourly forcast</div>

  <div class="forecast-panel" role="img" aria-label="Coastal landscape photo behind the hourly forecast table">
    <svg width="332" height="270" viewBox="0 0 332 270" font-family="Roboto, sans-serif">
      <g fill="#fff">
        <text x="20" y="30" font-size="13" font-weight="500">-1.0m</text><text x="20" y="42" font-size="8">Tide</text>
        <path d="M86 18l6 14h-12z" fill="#8fe3f5"/><text x="80" y="44" font-size="8">Wave</text>
        <text x="116" y="30" font-size="13" font-weight="500">0.3</text><text x="118" y="42" font-size="8">m</text>
        <text x="156" y="30" font-size="13" font-weight="500">12.6</text><text x="160" y="42" font-size="8">Sec</text>
      </g>
      <g fill="#fff" font-size="7" text-anchor="middle">
        <text x="66" y="74">08:00</text><text x="90" y="74">09:00</text><text x="114" y="74">10:00</text><text x="138" y="74">11:00</text><text x="162" y="74">12:00</text><text x="186" y="74">13:00</text><text x="210" y="74">14:00</text><text x="234" y="74">15:00</text><text x="258" y="74">16:00</text><text x="282" y="74">17:00</text><text x="306" y="74">18:00</text>
      </g>
      <text x="12" y="122" fill="#fff" font-size="11" font-weight="500">Wind</text>
      <g>
        <path d="M66 96l5 12h-10z" fill="#e8244f"/><path d="M90 96l5 12h-10z" fill="#5fd3a8"/><path d="M114 96l5 12h-10z" fill="#e8244f"/><path d="M138 96l5 12h-10z" fill="#f2d21c"/><path d="M162 96l5 12h-10z" fill="#f2d21c"/><path d="M186 96l5 12h-10z" fill="#5fd3a8"/><path d="M210 96l5 12h-10z" fill="#e8244f"/><path d="M234 96l5 12h-10z" fill="#f2d21c"/><path d="M258 96l5 12h-10z" fill="#5fd3a8"/><path d="M282 96l5 12h-10z" fill="#d9dde0"/><path d="M306 96l5 12h-10z" fill="#e8244f"/>
      </g>
      <g fill="#fff" font-size="8" text-anchor="middle">
        <text x="66" y="124">50</text><text x="90" y="124">30</text><text x="114" y="124">54</text><text x="138" y="124">20</text><text x="162" y="124">21</text><text x="186" y="124">34</text><text x="210" y="124">43</text><text x="234" y="124">12</text><text x="258" y="124">33</text><text x="282" y="124">23</text><text x="306" y="124">50</text>
      </g>
      <text x="12" y="180" fill="#fff" font-size="11" font-weight="500">Wave</text>
      <g>
        <circle cx="66" cy="160" r="4" fill="#2f7fd6"/><circle cx="90" cy="160" r="4" fill="#8fe3f5"/><circle cx="114" cy="160" r="4" fill="#2f7fd6"/><circle cx="138" cy="160" r="4" fill="#c4eefa"/><circle cx="162" cy="160" r="4" fill="#8fe3f5"/><circle cx="186" cy="160" r="4" fill="#8fe3f5"/><circle cx="210" cy="160" r="4" fill="#1a4fa8"/><circle cx="234" cy="160" r="4" fill="#c4eefa"/><circle cx="258" cy="160" r="4" fill="#c4eefa"/><circle cx="282" cy="160" r="4" fill="#1a4fa8"/><circle cx="306" cy="160" r="4" fill="#2f7fd6"/>
      </g>
      <g fill="#fff" font-size="8" text-anchor="middle">
        <text x="66" y="182">0.8</text><text x="90" y="182">0.3</text><text x="114" y="182">1.1</text><text x="138" y="182">0.1</text><text x="162" y="182">0.5</text><text x="186" y="182">0.5</text><text x="210" y="182">1.5</text><text x="234" y="182">0.2</text><text x="258" y="182">0.2</text><text x="282" y="182">2.5</text><text x="306" y="182">0.8</text>
      </g>
      <text x="12" y="238" fill="#fff" font-size="11" font-weight="500">Tide</text>
      <path d="M66 240C100 210 130 210 162 228S230 252 258 226 300 214 306 220" fill="none" stroke="#8fe3f5" stroke-width="2"/>
    </svg>
  </div>

  <nav class="tabbar">
    <div class="tab explore"><svg class="icon" width="16" height="16" viewBox="0 0 16 16"><circle cx="6.5" cy="6.5" r="5" fill="none" stroke="#2b3a44" stroke-width="1.6"/><path d="M10.5 10.5 15 15" stroke="#2b3a44" stroke-width="1.6"/></svg>Explore</div>
    <div class="tab calendar"><svg class="icon" width="24" height="24" viewBox="0 0 24 24"><rect x="3" y="5" width="18" height="16" rx="2" fill="none" stroke="#1d2830" stroke-width="1.6"/><path d="M3 10h18M8 3v4M16 3v4M7 13h2M11 13h2M15 13h2M7 17h2M11 17h2" stroke="#1d2830" stroke-width="1.6"/></svg></div>
    <div class="tab favorites"><svg class="icon" width="18" height="16" viewBox="0 0 18 16"><path d="M9 15S1 10 1 5a4 4 0 0 1 8-1 4 4 0 0 1 8 1c0 5-8 10-8 10z" fill="none" stroke="#2b3a44" stroke-width="1.4"/></svg>Favorites</div>
  </nav>
</section>

<!-- Daily outlook screen -->
<section class="screen outlook-screen" aria-label="Daily outlook">
  <div class="status"><span>9:41</span>
    <svg class="icon" width="46" height="12" viewBox="0 0 46 12"><g fill="#2b3a44"><rect x="0" y="8" width="3" height="4"/><rect x="5" y="5" width="3" height="7"/><rect x="10" y="2" width="3" height="10"/><path d="M18 5a9 9 0 0 1 12 0l-2 2a6 6 0 0 0-8 0z"/><rect x="33" y="2" width="12" height="8" rx="2"/></g></svg>
  </div>
  <div class="outlook-header">
    <svg class="icon menu" width="24" height="18" viewBox="0 0 24 18"><path d="M1 2h22M1 9h22M1 16h22" stroke="#2b3a44" stroke-width="2"/></svg>
    <div class="title">DAILY OUTLOOK</div>
    <svg class="icon add" width="20" height="20" viewBox="0 0 20 20"><circle cx="10" cy="10" r="8.5" fill="none" stroke="#2b3a44" stroke-width="1.5"/><path d="M10 5v10M5 10h10" stroke="#2b3a44" stroke-width="1.5"/></svg>
    <svg class="icon pin" width="16" height="20" viewBox="0 0 16 20"><path d="M8 0a7 7 0 0 1 7 7c0 5-7 13-7 13S1 12 1 7a7 7 0 0 1 7-7z" fill="#1d2830"/><circle cx="8" cy="7" r="2.5" fill="#fff"/></svg>
  </div>

  <div class="spot-list">
    <article class="spot-card">
      <div class="photo" role="img" aria-label="Cloudy sky photo of the spot"></div>
      <div class="info"><h3>Saltcombe</h3><div class="badges"><span class="badge live">Live</span><span class="badge good">Good</span></div><div class="dist">82Km</div>
        <svg class="icon heart" width="16" height="14" viewBox="0 0 18 16"><path d="M9 15S1 10 1 5a4 4 0 0 1 8-1 4 4 0 0 1 8 1c0 5-8 10-8 10z" fill="#fff"/></svg></div>
      <svg class="chart" width="200" height="96" viewBox="0 0 200 96">
        <text class="hours-label" x="0" y="92">Hours</text>
        <g stroke-linecap="round" stroke-width="7">
          <line x1="40" y1="76" x2="40" y2="70" stroke="#d9dde0"/><line x1="60" y1="76" x2="60" y2="68" stroke="#d9dde0"/><line x1="80" y1="76" x2="80" y2="64" stroke="#d9dde0"/><line x1="100" y1="76" x2="100" y2="48" stroke="#f2d21c"/><line x1="120" y1="76" x2="120" y2="44" stroke="#f2d21c"/><line x1="140" y1="76" x2="140" y2="36" stroke="#5fd3a8"/><line x1="160" y1="76" x2="160" y2="34" stroke="#d9dde0"/><line x1="180" y1="76" x2="180" y2="14" stroke="#5fd3a8"/>
        </g>
        <g class="hours-label" text-anchor="middle"><text x="40" y="92">08</text><text x="60" y="92">09</text><text x="80" y="92">10</text><text x="100" y="92">11</text><text x="120" y="92">12</text><text x="140" y="92">13</text><text x="160" y="92">14</text><text x="180" y="92">15</text></g>
      </svg>
    </article>

    <article class="spot-card">
      <div class="photo" role="img" aria-label="Cloudy sky photo of the spot"></div>
      <div class="info"><h3>Fenwick</h3><div class="badges"><span class="badge live">Live</span><span class="badge good">Good</span></div><div class="dist">99Km</div>
        <svg class="icon heart" width="16" height="14" viewBox="0 0 18 16"><path d="M9 15S1 10 1 5a4 4 0 0 1 8-1 4 4 0 0 1 8 1c0 5-8 10-8 10z" fill="#fff"/></svg></div>
      <svg class="chart" width="200" height="96" viewBox="0 0 200 96">
        <g stroke-linecap="round" stroke-width="7">
          <line x1="40" y1="76" x2="40" y2="70" stroke="#d9dde0"/><line x1="60" y1="76" x2="60" y2="68" stroke="#d9dde0"/><line x1="80" y1="76" x2="80" y2="54" stroke="#f2d21c"/><line x1="100" y1="76" x2="100" y2="48" stroke="#f2d21c"/><line x1="120" y1="76" x2="120" y2="40" stroke="#d9dde0"/><line x1="140" y1="76" x2="140" y2="34" stroke="#d9dde0"/><line x1="160" y1="76" x2="160" y2="46" stroke="#e8244f"/><line x1="180" y1="76" x2="180" y2="14" stroke="#d9dde0"/>
        </g>
        <g class="hours-label" text-anchor="middle"><text x="40" y="92">08</text><text x="60" y="92">09</text><text x="80" y="92">10</text><text x="100" y="92">11</text><text x="120" y="92">12</text><text x="140" y="92">13</text><text x="160" y="92">14</text><text x="180" y="92">15</text></g>
      </svg>
    </article>

    <article class="spot-card">
      <div class="photo" role="img" aria-label="Cloudy sky photo of the spot"></div>
      <div class="info"><h3>Elmfield Sports Ground</h3><div class="badges"><span class="badge live">Live</span><span class="badge light">Light</span></div><div class="dist">52Km</div>
        <svg class="icon heart" width="16" height="14" viewBox="0 0 18 16"><path d="M9 15S1 10 1 5a4 4 0 0 1 8-1 4 4 0 0 1 8 1c0 5-8 10-8 10z" fill="none" stroke="#fff" stroke-width="1.5"/></svg></div>
      <svg class="chart" width="200" height="96" viewBox="0 0 200 96">
        <g stroke-linecap="round" stroke-width="7">
          <line x1="40" y1="76" x2="40" y2="52" stroke="#5fd3a8"/><line x1="60" y1="76" x2="60" y2="68" stroke="#d9dde0"/><line x1="80" y1="76" x2="80" y2="50" stroke="#5fd3a8"/><line x1="100" y1="76" x2="100" y2="46" stroke="#f2d21c"/><line x1="120" y1="76" x2="120" y2="30" stroke="#e8244f"/><line x1="140" y1="76" x2="140" y2="40" stroke="#5fd3a8"/><line x1="160" y1="76" x2="160" y2="36" stroke="#d9dde0"/><line x1="180" y1="76" x2="180" y2="60" stroke="#d9dde0"/>
        </g>
        <g class="hours-label" text-anchor="middle"><text x="40" y="92">08</text><text x="60" y="92">09</text><text x="80" y="92">10</text><text x="100" y="92">11</text><text x="120" y="92">12</text><text x="140" y="92">13</text><text x="160" y="92">14</text><text x="180" y="92">15</text></g>
      </svg>
    </article>

    <article class="spot-card">
      <div class="photo" role="img" aria-label="Cloudy sky photo of the spot"></div>
      <div class="info"><h3>Harwell Beach</h3><div class="badges"><span class="badge live">Live</span><span class="badge strong">Strong</span></div><div class="dist">79Km</div>
        <svg class="icon heart" width="16" height="14" viewBox="0 0 18 16"><path d="M9 15S1 10 1 5a4 4 0 0 1 8-1 4 4 0 0 1 8 1c0 5-8 10-8 10z" fill="none" stroke="#fff" stroke-width="1.5"/></svg></div>
      <svg class="chart" width="200" height="96" viewBox="0 0 200 96">
        <g stroke-linecap="round" stroke-width="7">
          <line x1="40" y1="76" x2="40" y2="70" stroke="#d9dde0"/><line x1="60" y1="76" x2="60" y2="68" stroke="#d9dde0"/><line x1="80" y1="76" x2="80" y2="66" stroke="#d9dde0"/><line x1="100" y1="76" x2="100" y2="56" stroke="#f2d21c"/><line x1="120" y1="76" x2="120" y2="62" stroke="#f2d21c"/><line x1="140" y1="76" x2="140" y2="24" stroke="#5fd3a8"/><line x1="160" y1="76" x2="160" y2="40" stroke="#d9dde0"/><line x1="180" y1="76" x2="180" y2="46" stroke="#e8244f"/>
        </g>
        <g class="hours-label" text-anchor="middle"><text x="40" y="92">08</text><text x="60" y="92">09</text><text x="80" y="92">10</text><text x="100" y="92">11</text><text x="120" y="92">12</text><text x="140" y="92">13</text><text x="160" y="92">14</text><text x="180" y="92">15</text></g>
      </svg>
    </article>

    <article class="spot-card is-green">
      <div class="photo" role="img" aria-label="Photo of green coastal hills at the spot"></div>
      <div class="info"><h3>Cresting Beach</h3><div class="badges"><span class="badge live">Live</span><span class="badge bad">Bad</span></div><div class="dist">81Km</div>
        <svg class="icon heart" width="16" height="14" viewBox="0 0 18 16"><path d="M9 15S1 10 1 5a4 4 0 0 1 8-1 4 4 0 0 1 8 1c0 5-8 10-8 10z" fill="none" stroke="#fff" stroke-width="1.5"/></svg></div>
      <svg class="chart" width="200" height="96" viewBox="0 0 200 96">
        <g stroke-linecap="round" stroke-width="7">
          <line x1="40" y1="76" x2="40" y2="70" stroke="#5fd3a8"/><line x1="60" y1="76" x2="60" y2="66" stroke="#5fd3a8"/><line x1="80" y1="76" x2="80" y2="68" stroke="#d9dde0"/><line x1="100" y1="76" x2="100" y2="54" stroke="#f2d21c"/><line x1="120" y1="76" x2="120" y2="46" stroke="#e8244f"/><line x1="140" y1="76" x2="140" y2="40" stroke="#d9dde0"/><line x1="160" y1="76" x2="160" y2="36" stroke="#d9dde0"/><line x1="180" y1="76" x2="180" y2="32" stroke="#d9dde0"/>
        </g>
      </svg>
    </article>
  </div>

  <nav class="tabbar">
    <div class="tab explore"><svg class="icon" width="16" height="16" viewBox="0 0 16 16"><circle cx="6.5" cy="6.5" r="5" fill="none" stroke="#2b3a44" stroke-width="1.6"/><path d="M10.5 10.5 15 15" stroke="#2b3a44" stroke-width="1.6"/></svg>Explore</div>
    <div class="tab calendar"><svg class="icon" width="24" height="24" viewBox="0 0 24 24"><rect x="3" y="5" width="18" height="16" rx="2" fill="none" stroke="#1d2830" stroke-width="1.6"/><path d="M3 10h18M8 3v4M16 3v4M7 13h2M11 13h2M15 13h2M7 17h2M11 17h2" stroke="#1d2830" stroke-width="1.6"/></svg></div>
    <div class="tab favorites"><svg class="icon" width="18" height="16" viewBox="0 0 18 16"><path d="M9 15S1 10 1 5a4 4 0 0 1 8-1 4 4 0 0 1 8 1c0 5-8 10-8 10z" fill="none" stroke="#2b3a44" stroke-width="1.4"/></svg>Favorites</div>
  </nav>
</section>

</body>
</html>
```